I am a company selling interior designing materials

HI, I am selling interior design materials and require a namecard which is more outstanding while following a certain details placement as attached.

My clients are mainly interior designers so it has to attract their attention rather than feeling that its "just another namecard". I am selling wallcoverings, fabrics, acoustics and carpets.

Target Market(s)

interior designers designing hotels, commerical offices.

Contact Information for Business Card

As per attached.
Please change address to 47 Jalan 16 Tampines #05-02 Velmora Building Singapore 527314

Font styles to use
Other font styles liked:
• calibri

Requirements
Must have
• (1) company logo on top in the middle. Placement of contac details to be the same
• (2) company color is blue/green cymk 75/8/42/0
• (3) "KTV" logo to be prominent
• (4) You may change the logo but there should be a "swirl" surrounding the word KTV like current logo. The swirl pattern does not need to follow current logo and you may propose.
Should not have
• (1) there should not be any designs above "KTV" logo
• (2) no sharp triangles or angles

```html
<!DOCTYPE html>
<html lang="en">
<head>
<meta charset="utf-8">
<title>KTV Business Card</title>
<link rel="stylesheet" href="https://fonts.googleapis.com/css2?family=Carlito:wght@400;700&display=swap">
<style>
  :root {
    --teal: #1fb0a6;
    --red: #ed1c24;
    --grey: #5f5f5f;
    --white: #ffffff;
    --backdrop: #ece9e4;
  }
  * { box-sizing: border-box; margin: 0; padding: 0; }
  html, body { width: 1200px; height: 960px; overflow: hidden; }
  body {
    background: var(--backdrop);
    font-family: "Carlito", "Calibri", sans-serif;
    position: relative;
  }
  .card {
    position: absolute;
    left: 300px;
    width: 600px;
    height: 343px;
    background: var(--white);
    overflow: hidden;
    box-shadow: 0 6px 18px rgba(0,0,0,0.18);
  }
  .card--contact { top: 80px; }
  .card--brand { top: 520px; }

  /* contact side */
  .contact__brand {
    position: absolute;
    top: 38px;
    right: 40px;
    text-align: center;
  }
  .brand-name {
    font-weight: 700;
    color: var(--grey);
    letter-spacing: 2px;
  }
  .contact__brand .brand-name { font-size: 44px; line-height: 1; }
  .contact__company {
    margin-top: 6px;
    font-size: 13px;
    font-weight: 700;
    color: var(--grey);
  }
  .contact__person {
    position: absolute;
    left: 40px;
    top: 150px;
  }
  .contact__name {
    font-size: 30px;
    font-weight: 700;
    color: var(--red);
    letter-spacing: 1px;
  }
  .contact__phone {
    font-size: 17px;
    color: var(--teal);
    margin-top: 2px;
  }
  .contact__band {
    position: absolute;
    left: 0; right: 0; bottom: 0;
    height: 125px;
    background: var(--teal);
    border-top: 3px solid var(--red);
    padding: 26px 40px;
    color: var(--white);
    font-size: 16px;
    line-height: 1.7;
  }

  /* brand side */
  .brand__mark {
    position: absolute;
    top: 100px;
    left: 0; right: 0;
    text-align: center;
  }
  .brand__mark .brand-name { font-size: 76px; line-height: 1; }
  .brand__band {
    position: absolute;
    left: 0; right: 0; bottom: 0;
    height: 64px;
    background: var(--teal);
  }
  .brand__tab {
    position: absolute;
    left: 120px;
    bottom: 40px;
    width: 330px;
    height: 38px;
    background: var(--red);
    border-radius: 14px 14px 0 0;
    color: var(--white);
    font-weight: 700;
    font-size: 19px;
    line-height: 38px;
    text-align: center;
    letter-spacing: 0.5px;
    width: 380px;
  }
</style>
</head>
<body>

  <section class="card card--contact">
    <div class="contact__brand">
      <div class="brand-name">KTV</div>
      <div class="contact__company">Kestrel Textile Ventures Pte Ltd</div>
    </div>
    <div class="contact__person">
      <div class="contact__name">MAREN LIOE</div>
      <div class="contact__phone">+65 8127 4605</div>
    </div>
    <div class="contact__band">
      <p class="contact__email">maren@kestreltextile.com</p>
      <p class="contact__address">47 Jalan 16 Tampines #05-02 Velmora Building Singapore 527314</p>
    </div>
  </section>

  <section class="card card--brand">
    <div class="brand__mark">
      <div class="brand-name">KTV</div>
    </div>
    <div class="brand__band"></div>
    <div class="brand__tab">Wallcoverings | Acoustic | Fabrics | Carpet</div>
  </section>

</body>
</html>
```